Postcard Design

Postcard for the following:

Front of postcard:
A new little beauty and health haven has opened up just around the corner at 42 Larchmont Lane, Alder Heights.
Just like you, Maribel’s Nook is special, offering treatments and services tailor made to your specific needs. Maribel has over 24 years of industry experience and offers a unique approach to helping you feel healthful, nourished and happy. Her treatments are brilliantly effective and include remedial massage therapies and reflexology, gorgeous rejuvenating facials and much much more…………..come and experience this unique and 100% organic little piece of heaven.
You deserve to feel great so we work from the inside out by offering nutritional health advice and formulations developed especially for you. We wholly nourish the individual in the wise woman tradition of healing and happiness.
As a special welcome gift I would like to offer you $15 off any service
By appointment 027 5192604 I look forward to seeing you soon

Back of postcard:
The hearth has been the centre of human life for at least 400,000 years. it is the place where people meet to cook, eat, talk together and heal. The ' hearth' was the heart of the home It was the centre of activity, where everyone gathered to keep warm, laugh, listen to the stories of old and heal. It was the place of physical and emotional nourishment. The hearth is a symbol for the hospitality and living spirit of the home.

Industry/Entity Type

Hospitality

Requirements
Nice to have
• A logo for the business would be really good.

```html
<!DOCTYPE html>
<html lang="en">
<head>
<meta charset="utf-8">
<title>Maribel’s Nook – Postcard</title>
<link href="https://fonts.googleapis.com/css2?family=Questrial&display=swap" rel="stylesheet">
<style>
  :root {
    --bg: #c9c9cb;
    --card-light: #fbeef2;
    --card-white: #ffffff;
    --rose: #d13a78;
    --rose-deep: #c42a68;
    --rose-soft: #f3c9d8;
    --rose-pale: #f8dde7;
    --ink: #c2336f;
    --photo-a: #f6e3e8;
    --photo-b: #e9b9c9;
  }
  * { box-sizing: border-box; margin: 0; padding: 0; }
  html, body { width: 1058px; height: 1200px; overflow: hidden; }
  body {
    background: var(--bg);
    font-family: "Questrial", "Century Gothic", sans-serif;
    position: relative;
  }
  .postcard {
    position: absolute;
    left: 89px;
    width: 880px;
    height: 560px;
    overflow: hidden;
    box-shadow: 0 6px 18px rgba(0,0,0,.25);
  }
  .postcard--front { top: 30px; background: linear-gradient(180deg, var(--card-light), #f6dde6); }
  .postcard--back { top: 615px; background: linear-gradient(180deg, #f8e3ea 0%, var(--card-white) 75%); }
  .postcard svg.art { position: absolute; inset: 0; }

  .tagline {
    position: absolute; left: 443px; top: 167px; width: 400px; height: 36px;
    color: #fff; font-size: 13.5px; line-height: 18px; white-space: nowrap;
    transform: rotate(-8.8deg); transform-origin: center;
  }
  .intro {
    position: absolute; left: 40px; right: 40px; top: 274px;
    color: var(--ink); font-size: 14.5px; line-height: 19px; text-align: justify;
  }
  .intro p + p { margin-top: 10px; }
  .intro p.narrow { margin-right: 170px; }

  .brand {
    position: absolute; display: flex; align-items: center; gap: 8px;
    color: var(--rose); font-size: 18px;
  }
  .brand .dot { width: 14px; height: 14px; border-radius: 50%; background: var(--rose); }
  .postcard--front .brand { right: 36px; top: 392px; }
  .postcard--back .brand { left: 110px; top: 70px; }

  .offer-band {
    position: absolute; left: 0; right: 0; top: 432px; height: 88px;
    background: var(--rose-pale);
  }
  .offer-band::before {
    content: ""; position: absolute; right: 0; top: 0; width: 620px; height: 4px; background: var(--rose);
  }
  .offer {
    position: absolute; left: 0; right: 0; top: 444px;
    text-align: center; color: var(--rose-deep); font-size: 17px; line-height: 30px;
  }
  .badge {
    display: inline-block; vertical-align: middle; margin-left: 8px;
    width: 34px; height: 30px; line-height: 30px; border-radius: 50%;
    background: var(--rose); color: #fff; font-size: 14px; text-align: center;
  }
  .appointment-bar {
    position: absolute; left: 0; right: 0; bottom: 0; height: 40px;
    background: var(--rose); color: #fff; font-size: 16px; line-height: 40px; text-align: center;
  }

  .hearth-title {
    position: absolute; left: 50px; top: 115px; width: 240px; height: 28px;
    background: var(--rose); color: #fff; font-size: 17px; font-weight: 400; line-height: 28px; padding-left: 10px;
  }
  .hearth-text {
    position: absolute; left: 50px; top: 152px; width: 350px;
    color: var(--ink); font-size: 17px; line-height: 22px; text-align: justify;
  }
</style>
</head>
<body>

<section class="postcard postcard--front">
  <svg class="art" viewBox="0 0 880 560" width="880" height="560">
    <defs>
      <linearGradient id="photoTone" x1="0" y1="0" x2="1" y2="1">
        <stop offset="0" stop-color="var(--photo-a)"/>
        <stop offset="0.55" stop-color="#efcdd8"/>
        <stop offset="1" stop-color="var(--photo-b)"/>
      </linearGradient>
    </defs>
    <path role="img" aria-label="Spa photograph: woman relaxing during a massage beside candles, towels and pink blossoms"
          d="M0 0 H880 V110 C600 160 300 245 0 230 Z" fill="url(#photoTone)"/>
    <path d="M0 230 C300 245 600 160 880 110 V180 C600 225 300 270 0 250 Z" fill="var(--rose)"/>
    <path d="M0 250 C300 270 600 225 880 180 V188 C600 233 300 278 0 258 Z" fill="var(--rose-soft)"/>
  </svg>

  <p class="tagline">A new little beauty and health haven has opened up just<br>around the corner at 42 Larchmont Lane, Alder Heights.</p>

  <div class="intro">
    <p>Just like you, Maribel’s Nook is special, offering treatments and services tailor made to your specific needs. Maribel has over 24 years of industry experience and offers a unique approach to helping you feel healthful, nourished and happy. Her treatments are brilliantly effective and include remedial massage therapies and reflexology, gorgeous rejuvenating facials and much much more…………..come and experience this unique and 100% organic little piece of heaven.</p>
    <p class="narrow">You deserve to feel great so we work from the inside out by offering nutritional health advice and formulations developed especially for you. We wholly nourish the individual in the wise woman tradition of healing and happiness.</p>
  </div>

  <div class="brand"><span class="dot"></span>Maribel’s Nook</div>

  <div class="offer-band"></div>
  <p class="offer">As a special welcome gift I would like to offer you <span class="badge">$15</span><br>off any service</p>

  <div class="appointment-bar">By appointment 027 5192604 I look forward to seeing you soon</div>
</section>

<section class="postcard postcard--back">
  <svg class="art" viewBox="0 0 880 560" width="880" height="560">
    <path d="M40 50 C300 70 560 40 880 0 V10 C580 50 320 80 40 56 Z" fill="var(--rose)"/>
    <path d="M40 58 C320 82 590 52 880 14 V22 C600 62 330 90 40 62 Z" fill="var(--rose-soft)"/>
  </svg>

  <div class="brand"><span class="dot"></span>Maribel’s Nook</div>

  <h2 class="hearth-title">What is a hearth . . .</h2>
  <p class="hearth-text">The hearth has been the centre of human life for at least 400,000 years. It is the place where people meet to cook, eat and talk together and heal. The ‘hearth’ was the heart of the home. It was the centre of activity, where everyone gathered to eat and cook, to sit and warm themselves, and listen to the stories of old. It was the place of physical and emotional nourishment. The hearth is a symbol for the hospitality and living spirit of the home.</p>
</section>

</body>
</html>
```